Simple and clean poster/flyer design needed for public speaker!

SIMPLE AND CLEAN DESIGN NEEDED FOR POSTER/FLYER

I AM a public speaker based in London (www.corvanlethby.com)
and I would like to have a custom-made flyer/poster
(preferably in adobe CS4 template format) that I con customize (just changing the text) for my various speeches, topics and locations

I am looking for something very simple and clean.
NO extravagance or crowded poster, but a rather beautiful clean and eye-catching design that clearly informs people what i am talking about, where and when.

Go to my website www.corvanlethby.com
to see the colour scheme and style that I like
my poster should be like the website, similar colours, logo, clean, simple and clear.

Summary

(1) simple and clean design
(2) design that fits my brand (see website)
(3) clear and eye-catching to promote my speeches
(4) customizable for my various talks, by simply chancing the text (Please Adobe Photoshop CS4 template format)
(5)in A3, A4, A5, A6 sizes, so i can use it for both flyers and small posters

ADDITIONS

BIG BOLD HEADLINE TO GRAP ATTENTION, greatest prominence

sub headline to explain, smaller than the headline, but still prominent on the poster

just a few bullet points to list the benefits and answer the “whats in for me”-question
this is for people who are already interested and continue reading, medium prominence.

WHERE, WHEN, HOW MUCH-information, in the lower section of the poster, little text, but clearly visible

only one point of CONTACT on my poster “www.corvanlethby.com”, bit big and clear so that it is very prominent

little text, effectively used
LESS IS MORE
Updates

contact me regarding logo files and any questions you may have!

for the logo files go to

https://share.dropvaultex.net/f/x.aspx?k=41c07d2e9ab35f18c6d2

click on the folder "logo pack" to see the files

thanks for your interest. hope to see great designs!
I am really looking forward to it
if you have any questions, please do not hesitate to ask

Kind Regards
Corvan
 

• Simple, clean design, text sparingly used.

• The mood should be light-hearted, calm, bright, simple and friendly, comic like

• a lot of white space, calling more attention to the content

• a light blue, dark blue, white and black colour scheme as seen on the homepage (www.corvanlethby.com) please use the exact same colours as seen on the homepage.

White being most predominant, 2 different blue used to highlight something, black for text on white background.

• One graphic would be cool, as long as it is blue. It could be waves-like graphic, or something like the white pattern in the background, in my case just in blue on white background > http://www.quillmereretreathouse.org/., I do not mean exactly this graphic and not that crowded but a simple single graphic in blue as long as it fits the theme and feel of my poster

Top o f the poster

• (a )One short bold headline (TALK TITLE) with a sub-headline below it (hook)

• or (b) headline as question (…....?) and below sub-headline offering the solution (my talk ;-) of course)

• 3 benefits as on homepage, that I can adapt for each talk (bottom right of my start site “what are you looking for?” either blue on white, or as in the page white on blue...whatever looks better and fits the design). Not sure how that looks, and if to include it!

• the bottom of the poster will have “Where”-information “when”-information “ticket price” info

• contact at the very bottom...for more into or to purchase tickets (my website and email)

If you have any questions or need clarification please write me!

Requirements
Must have
• lot of white space
• less is more - simple design
• little text, little graphics- only used when necessary to greatest effect.
• light, friendly, modern feel
• blue-color scheme

```html
<!DOCTYPE html>
<html lang="en">
<head>
<meta charset="utf-8">
<title>Corvan Lethby – Talk Poster</title>
<link rel="stylesheet" href="https://fonts.googleapis.com/css2?family=Arimo:wght@400;700&display=swap">
<style>
  :root {
    --sky-deep: #2c66a8;
    --sky-mid: #4a86c6;
    --sky-light: #6aa3d8;
    --band-blue: #7ec0dc;
    --band-light: #a8d6ea;
    --band-edge: #6fb3d3;
    --panel: #e4f2f8;
    --ink: #1c2a38;
    --white: #ffffff;
  }
  * { margin: 0; padding: 0; box-sizing: border-box; }
  html, body { width: 848px; height: 1200px; overflow: hidden; background: var(--white); }
  body { font-family: "Arimo", Arial, sans-serif; font-weight: 700; color: var(--ink); }

  .poster { position: relative; width: 848px; height: 1200px; overflow: hidden; }

  .site-bar {
    position: absolute; left: 0; top: 0; width: 848px; height: 61px;
    background: var(--band-blue);
    display: flex; align-items: center; justify-content: center;
    font-size: 31px; letter-spacing: 2px; color: var(--ink);
  }

  .sky {
    position: absolute; left: 0; top: 61px; width: 848px; height: 944px;
    background:
      radial-gradient(ellipse 140px 90px at 730px 90px, rgba(255,255,255,.55), transparent 70%),
      radial-gradient(ellipse 110px 70px at 830px 30px, rgba(255,255,255,.5), transparent 70%),
      radial-gradient(ellipse 120px 160px at 820px 880px, rgba(255,255,255,.6), transparent 70%),
      radial-gradient(ellipse 130px 60px at 80px 900px, rgba(255,255,255,.45), transparent 70%),
      linear-gradient(180deg, var(--sky-deep) 0%, var(--sky-mid) 55%, var(--sky-light) 100%);
  }

  .hero-glow {
    position: absolute; left: 204px; top: 40px; width: 440px; height: 400px;
    background: radial-gradient(circle at 50% 45%, rgba(255,255,255,.98) 0%, rgba(255,255,255,.85) 18%, rgba(220,238,252,.45) 40%, rgba(255,255,255,0) 68%);
  }

  .quote {
    position: absolute; color: var(--white); font-size: 16px; line-height: 1.3;
    text-shadow: 0 1px 3px rgba(0,0,0,.35);
  }
  .quote--top-left { left: 21px; top: 128px; }
  .quote--right { left: 591px; top: 277px; }
  .quote--left { left: 40px; top: 332px; }
  .quote--footer { left: 0; width: 848px; top: 940px; text-align: center; }

  .affirmation {
    position: absolute; left: 0; width: 848px; top: 481px; text-align: center;
    color: var(--white); font-size: 21px; line-height: 1.4;
    text-shadow: 0 1px 3px rgba(0,0,0,.35);
  }
  .affirmation u { text-underline-offset: 3px; }

  .name-bubble {
    position: absolute; left: 172px; top: 570px; width: 502px; height: 124px;
    background: var(--band-blue); border-radius: 22px;
    box-shadow: 0 4px 12px rgba(0,0,0,.2);
    text-align: center;
  }
  .name-bubble__pointer { position: absolute; left: 401px; top: 692px; }
  .speaker-name { display: block; padding-top: 20px; font-size: 54px; line-height: 1; color: var(--ink);
    text-shadow: 0 2px 3px rgba(255,255,255,.4); }
  .speaker-tagline { display: block; margin-top: 4px; font-size: 17px; color: var(--white);
    text-shadow: 0 1px 2px rgba(0,0,0,.7); }

  .message-panel {
    position: absolute; left: 0; top: 713px; width: 779px; height: 205px;
    background: var(--panel); border-radius: 0 22px 22px 0;
    box-shadow: 0 4px 14px rgba(0,0,0,.2);
  }
  .headline {
    position: absolute; left: 64px; top: 56px; font-size: 48px; color: var(--white); letter-spacing: .3px;
    text-shadow: 1px 1px 0 #8d9aa4, 2px 3px 4px rgba(0,0,0,.45);
  }
  .subheadline { position: absolute; left: 72px; top: 126px; font-size: 25px; color: var(--ink); }

  .info-band {
    position: absolute; left: 0; top: 1005px; width: 848px; height: 195px;
    background: linear-gradient(180deg, var(--band-blue) 0%, var(--band-light) 100%);
    border-top: 9px solid var(--band-edge);
  }
  .event { position: absolute; left: 42px; top: 26px; }
  .event__intro, .event__place { font-size: 22px; color: var(--white); }
  .event__date { font-size: 37px; color: var(--ink); margin: 7px 0 6px; }

  .benefits { position: absolute; left: 524px; top: 26px; }
  .benefits__title { font-size: 22px; color: var(--ink); margin-bottom: 8px; }
  .benefits__list { list-style: none; font-size: 15px; color: var(--ink); line-height: 1.55; }
</style>
</head>
<body>
<main class="poster">
  <header class="site-bar">www.corvanlethby.com</header>

  <section class="sky" role="img" aria-label="Bright blue sky with soft white clouds"></section>
  <div class="hero-glow" role="img" aria-label="Radiant burst of light behind the speaker's joyful figure emblem"></div>

  <p class="quote quote--top-left">Nothing can happen to you that<br>is not for your highest good</p>
  <p class="quote quote--right">Life is a gift to enjoy,<br>not a struggle to endure!</p>
  <p class="quote quote--left">Life isn't happening to you,<br>it is happening for you!</p>

  <p class="affirmation">You are a beautiful expression of Life.<br>You are worthwhile because <u>you exist</u>!</p>

  <div class="name-bubble">
    <h1 class="speaker-name">Corvan Lethby</h1>
    <span class="speaker-tagline">Life is lived from the Inside-Out!</span>
  </div>
  <svg class="name-bubble__pointer" width="46" height="26" viewBox="0 0 46 26" aria-hidden="true">
    <path d="M0 0 L46 0 L23 26 Z" fill="#7ec0dc"/>
  </svg>

  <section class="message-panel">
    <h2 class="headline">Simple. Universal. Powerful.</h2>
    <p class="subheadline">Practical spirituality to transform your life.</p>
  </section>

  <p class="quote quote--footer">Don't wonder what the world will bring to you, but<br>choose what you will bring to the world.</p>

  <footer class="info-band">
    <div class="event">
      <p class="event__intro">New event on London</p>
      <p class="event__date">03 September 2010</p>
      <p class="event__place">Location - Harrowfield Arena</p>
    </div>
    <div class="benefits">
      <h3 class="benefits__title">What are you looking for?</h3>
      <ul class="benefits__list">
        <li>- improved self-esteem</li>
        <li>- inner peace and calm</li>
        <li>- greater purpose and meaning in life</li>
      </ul>
    </div>
  </footer>
</main>
</body>
</html>
```